complete redesign of prelmorax.com , responsive design

Present website should be used for ideation purpose, designer should submit best design which can explain visitor and excite them to download the app.
. By looking at default view of website, students should get the idea about product.

This website to explain about tablet app and it's features, benefits for students, parents and institutes.

This is tablet/Vexo based product to prepare National ( KMR, ZORWN, PUV, Brennick etc) and International competitive exams (YLD, KUW, QVF, DRUX etc) and visitor should get ideas by just looking at the home page.

Institutes can publish their content on Vornaplex.

Student can optimize time and performance on Vornaplex.

Content is same as present website and please use app screenshot to explain the product. screens should be used wherever relevant, refer attached screens. Website must be responsive and easy in navigation.
This is cloud based system and offering prep test , analysis and dynamic testing as per their study plan.

Education

Education

Coded - Design and coding required

5+ page

6b449b
886aae
b7a5cd
e4daeb
f3f1f8
ffffff

• Great design , responsive, easy to grasp the idea. Allow option to register for free app download.
• Project must have all pages as it is in present website.
• I will leave designer to come up with presentation.
• It should not be layout as it is today. Lot of design being submitted by changing just color and icons. I request to come up with your style and you can use contents from present website.

```html
<!DOCTYPE html>
<html lang="en">
<head>
<meta charset="utf-8">
<title>Vornaplex by Scorevault</title>
<link href="https://fonts.googleapis.com/css2?family=Open+Sans:wght@400;600;700&family=Roboto+Slab:wght@400;700&display=swap" rel="stylesheet">
<style>
:root{
  --purple:#6b449b;--purple-mid:#886aae;--lilac:#b7a5cd;--lilac-pale:#e4daeb;--mist:#f3f1f8;--white:#fff;
  --red:#e5213f;--ink:#3b3b4a;--grey:#777;--line:#e2e2e8;
  --blue:#2f9fe0;--green:#5fb548;--orange:#f39a1d;--pink:#e5467b;--teal:#2bb9b0;--violet:#8b5bc9;
}
*{box-sizing:border-box;margin:0;padding:0}
html,body{width:1200px;height:2980px;overflow:hidden}
body{font-family:"Open Sans",Arial,sans-serif;color:var(--ink);background:var(--white);position:relative}
a{color:inherit;text-decoration:none}
.header{position:absolute;top:0;left:0;width:1200px;height:60px;background:var(--white);display:flex;align-items:center;padding:0 60px;justify-content:space-between;box-shadow:0 1px 4px rgba(0,0,0,.08);z-index:2}
.brand{display:flex;align-items:center;gap:10px;font-weight:700;color:var(--purple);font-size:18px;letter-spacing:1px}
.brand .dot{width:36px;height:36px;border-radius:50%;background:var(--purple)}
.nav{display:flex;gap:34px;align-items:center;font-size:13px;color:var(--grey)}
.nav .active{color:var(--purple);font-weight:700;border-bottom:2px solid var(--purple);padding-bottom:4px}
.btn{display:inline-block;background:var(--red);color:var(--white);font-weight:600;border-radius:3px}
.nav .btn{background:var(--purple);padding:7px 16px;font-size:12px}
.hero{position:absolute;top:60px;left:0;width:1200px;height:760px;background:linear-gradient(90deg,#f7f5fa 0%,#ece8f1 45%,#d9d1e2 100%);overflow:hidden}
.hero-photo{position:absolute;right:0;top:0;width:720px;height:760px;background:linear-gradient(120deg,#e9e4ef 0%,#cdbfae 40%,#b89d85 60%,#8f7a9f 100%);opacity:.9}
.hero-copy{position:absolute;left:60px;top:300px;width:520px}
.hero-copy h1{font-family:"Roboto Slab",Georgia,serif;font-weight:400;font-size:46px;line-height:56px;color:var(--purple)}
.hero-copy p{margin-top:30px;font-size:17px;line-height:26px;color:var(--purple-mid);font-weight:600}
.hero-copy .btn{margin-top:42px;padding:14px 30px;font-size:16px}
.stores{margin-top:56px;display:flex;align-items:center;gap:12px;font-size:12px;color:var(--grey)}
.stores span.badge{width:34px;height:34px;border-radius:6px;background:var(--ink)}
.platform{position:absolute;top:820px;left:0;width:1200px;height:460px;background:var(--white);text-align:center}
.section-title{font-family:"Roboto Slab",Georgia,serif;font-size:26px;color:var(--purple);font-weight:700}
.platform .section-title{margin-top:34px}
.lead{width:900px;margin:12px auto 0;font-size:13px;line-height:20px;color:var(--grey)}
.tabs{display:inline-flex;margin-top:22px;border:1px solid var(--line);border-radius:3px;overflow:hidden}
.tabs span{padding:8px 30px;font-size:12px;font-weight:700;color:var(--red);border-right:1px solid var(--line)}
.tabs span:last-child{border-right:0}
.tabs .on{background:var(--mist);color:var(--purple)}
.features{display:grid;grid-template-columns:1fr 1fr;gap:22px 60px;width:1000px;margin:24px auto 0;text-align:left}
.feature{display:flex;gap:16px}
.diamond{flex:none;width:38px;height:38px;transform:rotate(45deg);border-radius:4px;margin:6px}
.feature h3{font-size:15px;color:var(--purple);font-weight:700}
.feature p{font-size:12px;line-height:17px;color:var(--grey);margin-top:3px}
.more{margin-top:22px;display:inline-block;font-size:11px;color:var(--grey);border:1px solid var(--line);padding:6px 18px;border-radius:3px}
.associates{position:absolute;top:1280px;left:0;width:1200px;height:70px;background:var(--mist);display:flex;align-items:center;padding:0 60px;gap:46px}
.associates strong{font-size:13px;color:var(--purple)}
.associates .badge{height:38px;border-radius:3px;background:var(--lilac)}
.easy{position:absolute;top:1350px;left:0;width:1200px;height:560px;background:linear-gradient(160deg,#2a7fc4 0%,#3d5fae 55%,var(--purple) 100%);color:var(--white)}
.easy .section-title{color:var(--white);text-align:center;margin-top:36px;font-weight:400}
.device{position:absolute;left:110px;top:120px;width:470px;height:380px;border-radius:30px;background:linear-gradient(135deg,#e6eef6,#b9c9dc)}
.promo{position:absolute;left:640px;top:120px;width:450px;height:250px;background:rgba(255,255,255,.12);border:1px solid rgba(255,255,255,.35);border-radius:4px;text-align:center}
.promo svg{margin-top:50px}
.promo small{display:block;margin-top:14px;font-size:12px;opacity:.85}
.promo b{display:block;font-family:"Roboto Slab",Georgia,serif;font-size:26px;color:#ffd447;margin-top:4px;font-weight:400}
.easy .note{position:absolute;left:640px;top:390px;width:450px;font-size:12px;line-height:19px;opacity:.85}
.need{position:absolute;top:1910px;left:0;width:1200px;height:730px;background:var(--white);text-align:center}
.need .section-title{margin-top:40px}
.cards{display:flex;gap:40px;justify-content:center;margin-top:40px}
.card{width:320px;height:480px;border:1px solid var(--line);border-radius:4px;background:var(--mist);position:relative;padding-top:78px}
.card .diamond{position:absolute;top:22px;left:50%;margin:0 0 0 -26px;width:52px;height:52px}
.card h3{font-size:20px;color:var(--purple);font-weight:700}
.card ul{list-style:none;text-align:left;margin:22px 26px 0}
.card li{font-size:12px;line-height:17px;color:var(--grey);padding:7px 0 7px 22px;border-bottom:1px solid var(--line);position:relative}
.card li svg{position:absolute;left:0;top:9px}
.card .btn{position:absolute;bottom:24px;left:50%;transform:translateX(-50%);padding:9px 24px;font-size:13px}
.totop{margin-top:36px;font-size:12px;color:var(--grey);font-style:italic}
.footer{position:absolute;top:2640px;left:0;width:1200px;height:340px;background:var(--purple);color:var(--lilac-pale)}
.cols{display:flex;gap:70px;padding:40px 60px 0}
.cols h4{font-family:"Roboto Slab",Georgia,serif;font-size:18px;color:var(--white);margin-bottom:16px}
.cols li{list-style:none;font-size:12px;line-height:24px}
.map{position:absolute;right:60px;top:56px;width:200px;height:120px;background:linear-gradient(135deg,#e9e6dc,#cfd8c2);border-radius:3px}
.social{position:absolute;right:60px;top:196px;display:flex;gap:8px}
.social span{width:24px;height:24px;border-radius:3px;background:var(--purple-mid)}
.copy{position:absolute;bottom:0;left:0;width:1200px;height:54px;background:#573583;font-size:11px;line-height:54px;text-align:center;color:var(--lilac)}
</style>
</head>
<body>
<header class="header">
  <div class="brand"><span class="dot"></span>SCOREVAULT</div>
  <nav class="nav">
    <a class="active">Home</a><a>Solution</a><a>Associates</a><a>FAQ</a><a>Our Products</a><a class="btn">JOIN US</a>
  </nav>
</header>

<section class="hero">
  <div class="hero-photo" role="img" aria-label="Smiling student with a tablet and books in a bright study room"></div>
  <div class="hero-copy">
    <h1>Exceed your results &amp; enhance your rank with Vornaplex.</h1>
    <p>Students save 30% time spent in analysing &amp; checking answers &amp; syllabus manually.</p>
    <a class="btn">Register Now</a>
    <div class="stores">App available on <span class="badge"></span><span class="badge"></span></div>
  </div>
</section>

<section class="platform">
  <h2 class="section-title">The Biggest Platform Ever</h2>
  <p class="lead">Vornaplex is a distinctive platform brought forth by Scorevault for all competitive exams. It provides a dedicated approach to score well in all competitive exams for the students of entire nation by accessing high quality content provided by leading institutes.</p>
  <div class="tabs"><span class="on">STUDENTS</span><span>INSTITUTES</span><span>PARENTS</span></div>
  <div class="features">
    <div class="feature"><span class="diamond" style="background:var(--blue)"></span><div><h3>Most Advanced Platform</h3><p>Vornaplex is a leading platform for students where they can get access to unlimited tests from top institutes anytime on their tablet.</p></div></div>
    <div class="feature"><span class="diamond" style="background:var(--pink)"></span><div><h3>Largest Reach at no extra cost</h3><p>Take advantage of biggest and fastest growing student database on Vornaplex with just your test packages and tests.</p></div></div>
    <div class="feature"><span class="diamond" style="background:var(--green)"></span><div><h3>Keep Student Focused</h3><p>Students can prefer the exam and practise on the tab, stay online or offline and focus on one goal.</p></div></div>
    <div class="feature"><span class="diamond" style="background:var(--orange)"></span><div><h3>Zero technology Investment</h3><p>Now institutes can focus on only educating and preparing the quality content and rest of things will be handled.</p></div></div>
    <div class="feature"><span class="diamond" style="background:var(--violet)"></span><div><h3>Class Practice on Tab</h3><p>Institutes can upload questions based on competitive exams and assign practice to classes.</p></div></div>
    <div class="feature"><span class="diamond" style="background:var(--teal)"></span><div><h3>Nationwide Marketing</h3><p>Vornaplex content is being marketed nationwide without any cost to the institute.</p></div></div>
  </div>
  <a class="more">KNOW MORE ›</a>
</section>

<section class="associates">
  <strong>Associates:</strong>
  <span class="badge" style="width:150px"></span>
  <span class="badge" style="width:170px"></span>
  <span class="badge" style="width:160px"></span>
  <span class="badge" style="width:150px"></span>
</section>

<section class="easy">
  <h2 class="section-title">Easy to Use</h2>
  <div class="device" role="img" aria-label="Hand holding a Vexo tablet showing the Vornaplex app home screen"></div>
  <div class="promo">
    <svg width="70" height="70" viewBox="0 0 70 70"><circle cx="35" cy="35" r="32" fill="none" stroke="#fff" stroke-width="3"/><path d="M28 22 L50 35 L28 48 Z" fill="#fff"/></svg>
    <small>Spend some time getting to know</small>
    <b>Watch The Promo</b>
  </div>
  <p class="note">Large number of students for KMR, ZORWN, PUV, Brennick, YLD, KUW, QVF and DRUX prepare on Vornaplex. Offline practice, instant analysis and dynamic tests fit every study plan on the cloud.</p>
</section>

<section class="need">
  <h2 class="section-title">Everything You Need</h2>
  <p class="lead">Vornaplex is a broad platform for the students, institutes and parents to come together to explore the opportunities and to augment the entire education system in an innovative direction. Students can now crack the exams with big scores by accessing the high quality content and institutes can also save the monetary benefits by using the large student database free of cost.</p>
  <div class="cards">
    <div class="card"><span class="diamond" style="background:var(--blue)"></span><h3>Students</h3>
      <ul>
        <li><svg width="12" height="10"><path d="M1 5l3 3 7-7" stroke="#5fb548" stroke-width="2" fill="none"/></svg>Outstanding platform for the preparation of competitive exams</li>
        <li><svg width="12" height="10"><path d="M1 5l3 3 7-7" stroke="#5fb548" stroke-width="2" fill="none"/></svg>Access of result analysis direct from the leading institutes</li>
        <li><svg width="12" height="10"><path d="M1 5l3 3 7-7" stroke="#5fb548" stroke-width="2" fill="none"/></svg>Real time analysis of the test preparation</li>
        <li><svg width="12" height="10"><path d="M1 5l3 3 7-7" stroke="#5fb548" stroke-width="2" fill="none"/></svg>Tracks time to solve each question</li>
        <li><svg width="12" height="10"><path d="M1 5l3 3 7-7" stroke="#5fb548" stroke-width="2" fill="none"/></svg>Offline accessibility of tests, save your all class content</li>
      </ul><a class="btn">Know More</a></div>
    <div class="card"><span class="diamond" style="background:var(--green)"></span><h3>Institutes</h3>
      <ul>
        <li><svg width="12" height="10"><path d="M1 5l3 3 7-7" stroke="#5fb548" stroke-width="2" fill="none"/></svg>Complete encryption of listings</li>
        <li><svg width="12" height="10"><path d="M1 5l3 3 7-7" stroke="#5fb548" stroke-width="2" fill="none"/></svg>Zero technology investment</li>
        <li><svg width="12" height="10"><path d="M1 5l3 3 7-7" stroke="#5fb548" stroke-width="2" fill="none"/></svg>Programs &amp; test packs at your own cost</li>
        <li><svg width="12" height="10"><path d="M1 5l3 3 7-7" stroke="#5fb548" stroke-width="2" fill="none"/></svg>Full control of access and visibility</li>
        <li><svg width="12" height="10"><path d="M1 5l3 3 7-7" stroke="#5fb548" stroke-width="2" fill="none"/></svg>Sell your content nationwide</li>
        <li><svg width="12" height="10"><path d="M1 5l3 3 7-7" stroke="#5fb548" stroke-width="2" fill="none"/></svg>Offer reports to students with high test rating</li>
      </ul><a class="btn">Know More</a></div>
    <div class="card"><span class="diamond" style="background:var(--pink)"></span><h3>Parents</h3>
      <ul>
        <li><svg width="12" height="10"><path d="M1 5l3 3 7-7" stroke="#5fb548" stroke-width="2" fill="none"/></svg>Monitor all your kids in a single platform</li>
        <li><svg width="12" height="10"><path d="M1 5l3 3 7-7" stroke="#5fb548" stroke-width="2" fill="none"/></svg>Access child's performance data anytime</li>
        <li><svg width="12" height="10"><path d="M1 5l3 3 7-7" stroke="#5fb548" stroke-width="2" fill="none"/></svg>Check the success level of your child</li>
        <li><svg width="12" height="10"><path d="M1 5l3 3 7-7" stroke="#5fb548" stroke-width="2" fill="none"/></svg>See complete insight of test results</li>
        <li><svg width="12" height="10"><path d="M1 5l3 3 7-7" stroke="#5fb548" stroke-width="2" fill="none"/></svg>Get encouragement from your child</li>
        <li><svg width="12" height="10"><path d="M1 5l3 3 7-7" stroke="#5fb548" stroke-width="2" fill="none"/></svg>Analyse test and live progress in time</li>
      </ul><a class="btn">Know More</a></div>
  </div>
  <p class="totop">Click here to go to top ↑</p>
</section>

<footer class="footer">
  <div class="cols">
    <div><h4>General</h4><ul><li>Home</li><li>About Us</li><li>FAQ</li><li>Contact Us</li></ul></div>
    <div><h4>Our Products</h4><ul><li>Vornaplex</li></ul></div>
    <div><h4>Learn More</h4><ul><li>Terms &amp; Conditions</li><li>Privacy Policy</li><li>Sitemap</li></ul></div>
    <div><h4>Quick Contact</h4><ul><li>14 Orvane Street, Kestrel Park</li><li>+91 40 5583 2190</li><li>hello@prelmorax.com</li></ul></div>
  </div>
  <div class="map" role="img" aria-label="Street map showing the office location"></div>
  <div class="social"><span></span><span></span><span></span><span></span></div>
  <div class="copy">Copyright © 2014 Scorevault Pvt Ltd. All rights reserved.</div>
</footer>
</body>
</html>
```